I work in the manufacturing industry and currently for TK in the wind department. I'm a contractor. So no TK symbol can be on the card but I can put a wind turbine on it. I am a skydiver as well, so I want a skydiver in the parachute floating next to a turbine with some clouds, the sun over head and the ground below. Hits the moto.

Quality inspection and manufacturing is the industry I work in.

Industry

Harold Tavisky
MQI (manufacturing Quality Inspector)
"Analyzing Quality from a different angle!"

Lumo48213@mailvista.net
555-382-1974

Must have
• Skydiver in parachute, wind turbine, clouds, the sun and the ground. If you can come up with a better moto, please let me know. The back side display "CobleFen inc" in small text in a corner.

```html
<!DOCTYPE html>
<html lang="en">
<head>
<meta charset="utf-8">
<title>Harold Tavisky – Business Card</title>
<link href="https://fonts.googleapis.com/css2?family=Fira+Sans:wght@400;600&family=Tinos&display=swap" rel="stylesheet">
<style>
  :root {
    --page-bg: #e9e9e9;
    --card-front: #6f6f6f;
    --ground-far: #3a3a3a;
    --ground-near: #262626;
    --text-light: #f2f2f2;
    --text-muted: #d0d0d0;
    --card-back: #1c1c1c;
    --rule: #cfcfcf;
    --scene-top: #8a8a8a;
    --scene-bottom: #5a5a5a;
  }
  * { box-sizing: border-box; margin: 0; padding: 0; }
  html, body {
    width: 1200px; height: 1200px; overflow: hidden;
    background: var(--page-bg);
  }
  .sheet {
    width: 1200px; height: 1200px;
    display: flex; align-items: center; justify-content: center; gap: 40px;
  }
  .card {
    position: relative;
    width: 540px; height: 309px;
    overflow: hidden;
    box-shadow: 0 6px 18px rgba(0,0,0,.18);
  }
  .card-front { background: var(--card-front); font-family: "Fira Sans", sans-serif; color: var(--text-light); }
  .ground { position: absolute; inset: 0; width: 100%; height: 100%; }
  .tagline {
    position: absolute; left: 36px; top: 40px;
    font-size: 16px; font-weight: 600; color: var(--text-muted);
    white-space: nowrap;
  }
  .name {
    position: absolute; left: 36px; top: 96px;
    font-size: 20px; font-weight: 600;
  }
  .title {
    position: absolute; left: 36px; top: 122px;
    font-size: 13px; color: var(--text-muted);
  }
  .contacts {
    position: absolute; left: 130px; top: 200px;
    list-style: none; font-size: 14px; line-height: 20px;
    white-space: nowrap;
  }
  .contacts li { display: flex; align-items: center; gap: 6px; }
  .contacts svg { width: 14px; height: 14px; flex: none; }
  .scene-art {
    position: absolute; left: 380px; top: 76px; width: 132px; height: 200px;
    background: linear-gradient(180deg, var(--scene-top), var(--scene-bottom));
    border-radius: 6px;
  }
  .card-back { background: var(--card-back); font-family: "Tinos", serif; }
  .back-footer {
    position: absolute; left: 0; right: 28px; bottom: 34px;
    display: flex; align-items: flex-end; gap: 10px;
  }
  .rule {
    flex: 1; height: 1px; margin-bottom: 9px;
    background: var(--rule);
  }
  .company {
    font-size: 17px; color: var(--text-light); white-space: nowrap;
  }
</style>
</head>
<body>
<main class="sheet">
  <section class="card card-front">
    <svg class="ground" viewBox="0 0 540 309" preserveAspectRatio="none" aria-hidden="true">
      <path d="M0 160 C120 120 220 150 330 185 L540 215 L540 309 L0 309 Z" fill="var(--ground-far)"/>
      <path d="M0 215 C150 185 300 230 540 245 L540 309 L0 309 Z" fill="var(--ground-near)"/>
    </svg>
    <p class="tagline">Analyzing Quality from a different angle!</p>
    <h1 class="name">Harold Tavisky MQI</h1>
    <p class="title">(Manufacturing Quality Inspector)</p>
    <ul class="contacts">
      <li>
        <svg viewBox="0 0 14 14" aria-hidden="true"><circle cx="7" cy="7" r="7" fill="var(--text-muted)"/><rect x="3.5" y="4.5" width="7" height="5" fill="none" stroke="#333" stroke-width="1"/><path d="M3.5 4.5 L7 7.5 L10.5 4.5" fill="none" stroke="#333" stroke-width="1"/></svg>
        Lumo48213@mailvista.net
      </li>
      <li>
        <svg viewBox="0 0 14 14" aria-hidden="true"><circle cx="7" cy="7" r="7" fill="var(--text-muted)"/><path d="M4.5 3.5 L6 3.5 L6.5 5.5 L5.5 6.3 C6 7.5 6.5 8 7.7 8.5 L8.5 7.5 L10.5 8 L10.5 9.5 C7 10 4 7 4.5 3.5 Z" fill="#333"/></svg>
        555-382-1974
      </li>
    </ul>
    <div class="scene-art" role="img" aria-label="Illustration of a skydiver under a parachute floating beside a wind turbine, with clouds and the sun overhead"></div>
  </section>

  <section class="card card-back">
    <div class="back-footer">
      <div class="rule"></div>
      <p class="company">CobleFen inc</p>
    </div>
  </section>
</main>
</body>
</html>
```